Slider images for online fax service homepage

Qlipo® needs 4 slider images for our newly designed homepage. The slider images should convey professionalism and simplicity without feeling cold or stuffy. The 4th slide is the only one that will contain a video and should be designed with that in mind. Attached to this contest, you will find two .pdf files. One contains a mockup of the new homepage containing dimensions and font requirements. The other is a spreadsheet containing copy for each slide.
In case you are unfamiliar with the brand, Qlipo® is the industry leader in online fax services. We provide faxing capabilities from mobile phones, tablets, and computers with state-of-the-art functionality, such as the ability to sign documents with your finger and send a document to any fax number directly from email.
Updates

FYI:  The dimensions of the video are 640x360.

Hello designers,

We don't want you to think we've forgotten about this contest.  We've been delayed in user testing but hope to have a response soon.

Thank you.

Target Market(s)

Mobile professionals and small businesses who need 24/7 access to fax services, such as lawyers, realtors, truckers, etc.

Industry/Entity Type

Industry

Requirements
Must have
• • The final deliverable should consist of a layered .psd file.
• Dimensions : 1500x475 (viewable area is 1200x475)
• Font is Google font – Lato
• Headline 62pt
• Subhead 32 pt

```html
<!DOCTYPE html>
<html lang="en">
<head>
<meta charset="utf-8">
<title>The Fast, Smart and Secure Way to Fax</title>
<link href="https://fonts.googleapis.com/css2?family=Lato:wght@100;300;400;700&display=swap" rel="stylesheet">
<style>
  :root {
    --ink-light: #ffffff;
    --bg-deep: #2e4656;
    --bg-mid: #5b7d90;
    --bg-soft: #9fb6c2;
    --bg-haze: #c9d6dc;
    --skin-light: #e4c9bc;
    --skin-mid: #caa08f;
    --text-shadow: rgba(10, 25, 35, 0.45);
  }
  html, body {
    margin: 0;
    padding: 0;
    width: 1200px;
    height: 380px;
    overflow: hidden;
    background: var(--bg-deep);
  }
  .slide {
    position: relative;
    width: 1200px;
    height: 380px;
    overflow: hidden;
    font-family: "Lato", Arial, sans-serif;
    color: var(--ink-light);
  }
  .slide__photo {
    position: absolute;
    inset: 0;
    background:
      radial-gradient(ellipse 260px 150px at 1000px 130px, var(--skin-light) 0%, rgba(228, 201, 188, 0) 100%),
      radial-gradient(ellipse 200px 120px at 880px 220px, var(--skin-mid) 0%, rgba(202, 160, 143, 0) 100%),
      radial-gradient(ellipse 170px 60px at 560px 180px, var(--skin-light) 0%, rgba(228, 201, 188, 0) 100%),
      radial-gradient(ellipse 220px 120px at 1150px 240px, var(--bg-haze) 0%, rgba(201, 214, 220, 0) 100%),
      radial-gradient(ellipse 300px 110px at 500px 340px, var(--bg-soft) 0%, rgba(159, 182, 194, 0) 100%),
      linear-gradient(100deg, var(--bg-deep) 0%, var(--bg-mid) 45%, var(--bg-soft) 75%, var(--bg-mid) 100%);
  }
  .slide__icon {
    position: absolute;
    left: 322px;
    top: 262px;
    width: 110px;
    height: 92px;
  }
  .slide__copy {
    position: absolute;
    left: 20px;
    top: 0;
    text-shadow: 0 1px 3px var(--text-shadow);
  }
  .headline {
    margin: 8px 0 0;
    font-size: 60px;
    line-height: 72px;
    font-weight: 100;
    letter-spacing: -0.5px;
  }
  .headline strong {
    font-weight: 400;
  }
  .subhead {
    margin: 38px 0 0;
    font-size: 20px;
    line-height: 24px;
    font-weight: 400;
  }
</style>
</head>
<body>
  <main class="slide">
    <div class="slide__photo" role="img" aria-label="Close-up photo of a hand touching a glowing tablet screen on a soft blue background"></div>

    <svg class="slide__icon" viewBox="0 0 100 90" aria-hidden="true">
      <g transform="rotate(-28 50 45)" fill="none" stroke="#ffffff" stroke-width="2.4" stroke-linejoin="round" opacity="0.9">
        <rect x="14" y="24" width="72" height="44"/>
        <polyline points="14,24 50,52 86,24"/>
      </g>
    </svg>

    <section class="slide__copy">
      <h1 class="headline">The <strong>Fast</strong>, <strong>Smart</strong><br>And <strong>Secure</strong> Way to <strong>Fax</strong></h1>
      <p class="subhead">Send And Receive Faxes<br>Easily And Securely By Email.<br>No Paper Needed.</p>
    </section>
  </main>
</body>
</html>
```